Real Estate Investment Company

Design Powerpoint slides are consistent with our logo, colors, and typeface. These Powerpoint slides will be used in all aspects of the business from live presentations to presentation decks available on a website or via email. Need to have different slide types created that allow for different types of slides such as cover pages, text heavy pages, image and chart heavy pages, multiple column pages, and mixed content pages.
Updates

Reason: to give additional time to get the design correct. I plan on making a selection in the next day or 2

Target Market(s)

Real Estate Investors

Industry/Entity Type

Investment

Other font styles liked:
• Consistent with logo

Requirements
Must have
• Our colors
• Our logo where possible
• Different slide designs of the same theme to allow for different types of slides such as cover pages, text heavy, picture heavy, and mixed content.
• Slides in both portrait and landscape orientation
Nice to have

```html
<!DOCTYPE html>
<html lang="en">
<head>
<meta charset="utf-8">
<title>Ridgeline Holdings – Slide Theme</title>
<link rel="stylesheet" href="https://fonts.googleapis.com/css2?family=Montserrat:wght@800&family=Roboto:wght@300&family=Open+Sans:wght@400;600;700&display=swap">
<style>
:root{
  --navy:#2f3382;
  --navy-deep:#262a6e;
  --blue-mid:#4a53b6;
  --ink:#333;
  --grey:#8a8a8a;
  --grey-light:#cfd0d8;
  --track:#e2e2e6;
  --white:#fff;
}
*{margin:0;padding:0;box-sizing:border-box}
html,body{width:1200px;height:950px;overflow:hidden;background:var(--white);font-family:"Open Sans",sans-serif;color:var(--ink)}
.sheet{position:relative;width:1200px;height:950px}
.slide{position:absolute;width:366px;height:206px;background:var(--white);overflow:hidden;box-shadow:0 2px 10px rgba(0,0,0,.28)}
.c1{left:24px}.c2{left:417px}.c3{left:810px}
.r1{top:26px}.r2{top:254px}.r3{top:486px}.r4{top:717px}
.abs{position:absolute}

/* header band */
.hdr{position:absolute;left:0;top:0;width:100%;height:42px;background:var(--navy);color:var(--white)}
.hdr-title{position:absolute;left:15px;top:9px;font-family:"Roboto",sans-serif;font-weight:300;font-size:14px;letter-spacing:.2px;white-space:nowrap}
.hdr-sub{position:absolute;left:15px;top:29px;font-size:6px;font-weight:700}
.brand{position:absolute;display:flex;align-items:center;gap:3px;font-family:"Open Sans",sans-serif;font-weight:600;text-transform:uppercase;white-space:nowrap}
.brand-mark{display:inline-block;background:currentColor}
.hdr .brand{right:10px;top:16px;font-size:5.5px;color:var(--white)}
.hdr .brand-mark{width:6px;height:6px}

.ftr{position:absolute;left:9px;bottom:4px;font-size:4.5px;letter-spacing:.8px;color:var(--grey)}
.pg{position:absolute;right:8px;bottom:0;width:12px;height:9px;background:var(--navy);color:var(--white);font-size:4px;text-align:center;line-height:9px}
.base-line{position:absolute;left:0;bottom:0;width:100%;height:1px;background:var(--navy)}

.lead{position:absolute;left:40px;right:40px;top:50px;font-size:5.6px;line-height:1.45;text-align:center}
.tiny{font-size:4px;line-height:1.4;color:var(--grey)}
.label{font-size:5.2px;font-weight:700;color:var(--navy);text-transform:uppercase}

/* cover slides */
.photo{position:absolute}
.big-title{font-family:"Montserrat",sans-serif;font-weight:800;color:var(--navy);line-height:1.18;text-transform:uppercase}
.divider{position:absolute;width:1px;background:#ddd}

/* bullets */
.bullet{position:absolute;width:100px;padding-left:13px}
.bullet::before{content:"";position:absolute;left:0;top:2px;width:3px;height:3px;border-radius:50%;background:var(--navy)}
.bullet .label{font-size:6px;margin-bottom:2px}

/* team */
.member{position:absolute;width:70px;text-align:center}
.portrait{width:48px;height:48px;border-radius:50%;margin:0 auto 6px;border:1px solid var(--grey-light);background:radial-gradient(circle at 50% 40%,#c9b7a6 0 30%,#3d3b44 31% 60%,#e9e9ee 61%)}

/* icon circles */
.feature{position:absolute;width:70px;text-align:center}
.icon-disc{width:46px;height:46px;border-radius:50%;background:var(--navy);margin:0 auto 8px;display:flex;align-items:center;justify-content:center;border:2px solid #d9dbee}

/* petals */
.petal{position:absolute;width:56px;height:56px;background:var(--navy);display:flex;align-items:center;justify-content:center}
.p-tl{border-radius:50% 50% 0 50%}.p-tr{border-radius:50% 50% 50% 0}
.p-bl{border-radius:50% 0 50% 50%}.p-br{border-radius:0 50% 50% 50%}
.petal-note{position:absolute;width:70px;font-size:4.6px;line-height:1.35;color:var(--grey)}
.petal-note b{display:block;color:var(--ink);font-size:5.4px;font-weight:600;margin-bottom:2px}
.right-note{text-align:left}.left-note{text-align:right}

/* unit chart */
.units{position:absolute;display:flex;gap:6px}
.unit{width:13px;height:34px;border-radius:6px 6px 2px 2px;background:var(--navy)}
.unit.off{background:#d8d9e2}
.unit-val{position:absolute;font-size:14px;font-weight:700;color:var(--navy)}

/* table */
.data{position:absolute;left:22px;top:56px;width:322px;border-collapse:collapse;font-size:5.5px}
.data th{background:var(--navy);color:var(--white);font-weight:700;height:12px;border-right:1px solid #5a5fa0}
.data td{height:12.5px;text-align:center;color:var(--grey);font-size:4.4px;border-bottom:1px solid #ddd;border-right:1px solid #ddd}
.data td:first-child{text-align:left;padding-left:18px;color:var(--ink);font-size:5.5px}
.data tr.total td{background:#e6e6ea}
.data{border:1px solid #999}

/* donuts */
.stat{position:absolute;width:70px;text-align:center;top:60px}
.stat .amount{font-size:9px;margin-top:3px;color:#555}
.stat .tiny{margin-top:2px;color:#999}

/* dark slides */
.dark{background:var(--navy)}
.dark-text{position:absolute;color:var(--white)}
</style>
</head>
<body>
<div class="sheet">

<!-- 1 cover with photo -->
<section class="slide c1 r1">
  <div class="photo" role="img" aria-label="Warm living room interior with sofa, lamp and bookshelves" style="left:0;top:0;width:366px;height:132px;background:linear-gradient(100deg,#3b2114 0%,#6d3b1f 35%,#c77a35 60%,#e8b377 80%,#f4e3c8 100%)"></div>
  <div class="brand" style="left:37px;top:163px;font-size:6px;color:var(--navy)"><span class="brand-mark" style="width:6px;height:6px"></span>Ridgeline Holdings</div>
  <div class="divider" style="left:140px;top:140px;height:56px"></div>
  <div class="big-title abs" style="left:158px;top:150px;font-size:13px">Presentation Title<br>Goes Here</div>
  <div class="abs" style="left:158px;top:185px;font-size:5.5px;font-weight:700;color:var(--navy-deep)">Your Subtitle Goes Here</div>
</section>

<!-- 2 plain cover -->
<section class="slide c2 r1">
  <div class="brand" style="left:34px;top:116px;font-size:6px;color:var(--navy)"><span class="brand-mark" style="width:6px;height:6px"></span>Ridgeline Holdings</div>
  <div class="divider" style="left:138px;top:45px;height:120px"></div>
  <div class="big-title abs" style="left:162px;top:76px;font-size:15.5px">Presentation<br>Title Goes Here</div>
  <div class="abs" style="left:164px;top:123px;font-size:5.5px;font-weight:700">Your Subtitle Goes Here</div>
</section>

<!-- 3 bullet grid -->
<section class="slide c3 r1">
  <header class="hdr"><div class="hdr-title">PRESENTATION TITLE GOES HERE</div><div class="hdr-sub">Subtitle goes here</div><div class="brand"><span class="brand-mark"></span>Ridgeline Holdings</div></header>
  <div class="bullet" style="left:14px;top:50px"><div class="label">Bullet Heading</div><p class="tiny">Lorem ipsum dolor sit amet, consectetur adipiscing elit. Aliquam lacus justo, vulputate consequat laoreet eget, hendrerit in metus.</p></div>
  <div class="bullet" style="left:133px;top:50px"><div class="label">Bullet Heading</div><p class="tiny">Lorem ipsum dolor sit amet, consectetur adipiscing elit. Aliquam lacus justo, vulputate consequat laoreet eget, hendrerit in metus.</p></div>
  <div class="bullet" style="left:252px;top:50px"><div class="label">Bullet Heading</div><p class="tiny">Lorem ipsum dolor sit amet, consectetur adipiscing elit. Aliquam lacus justo, vulputate consequat laoreet eget, hendrerit in metus.</p></div>
  <div class="bullet" style="left:14px;top:88px"><div class="label">Bullet Heading</div><p class="tiny">Lorem ipsum dolor sit amet, consectetur adipiscing elit. Aliquam lacus justo, vulputate consequat laoreet eget, hendrerit in metus.</p></div>
  <div class="bullet" style="left:133px;top:88px"><div class="label">Bullet Heading</div><p class="tiny">Lorem ipsum dolor sit amet, consectetur adipiscing elit. Aliquam lacus justo, vulputate consequat laoreet eget, hendrerit in metus.</p></div>
  <div class="bullet" style="left:252px;top:88px"><div class="label">Bullet Heading</div><p class="tiny">Lorem ipsum dolor sit amet, consectetur adipiscing elit. Aliquam lacus justo, vulputate consequat laoreet eget, hendrerit in metus.</p></div>
  <div class="bullet" style="left:14px;top:126px"><div class="label">Bullet Heading</div><p class="tiny">Lorem ipsum dolor sit amet, consectetur adipiscing elit. Aliquam lacus justo, vulputate consequat laoreet eget, hendrerit in metus.</p></div>
  <div class="bullet" style="left:133px;top:126px"><div class="label">Bullet Heading</div><p class="tiny">Lorem ipsum dolor sit amet, consectetur adipiscing elit. Aliquam lacus justo, vulputate consequat laoreet eget, hendrerit in metus.</p></div>
  <div class="bullet" style="left:252px;top:126px"><div class="label">Bullet Heading</div><p class="tiny">Lorem ipsum dolor sit amet, consectetur adipiscing elit. Aliquam lacus justo, vulputate consequat laoreet eget, hendrerit in metus.</p></div>
  <div class="bullet" style="left:14px;top:165px"><div class="label">Bullet Heading</div><p class="tiny">Lorem ipsum dolor sit amet, consectetur adipiscing elit. Aliquam lacus justo, vulputate consequat laoreet eget, hendrerit in metus.</p></div>
  <div class="bullet" style="left:133px;top:165px"><div class="label">Bullet Heading</div><p class="tiny">Lorem ipsum dolor sit amet, consectetur adipiscing elit. Aliquam lacus justo, vulputate consequat laoreet eget, hendrerit in metus.</p></div>
  <div class="bullet" style="left:252px;top:165px"><div class="label">Bullet Heading</div><p class="tiny">Lorem ipsum dolor sit amet, consectetur adipiscing elit. Aliquam lacus justo, vulputate consequat laoreet eget, hendrerit in metus.</p></div>
  <div class="ftr">www.ridgelineholdings.com</div><div class="pg">11</div><div class="base-line"></div>
</section>

<!-- 4 team -->
<section class="slide c1 r2">
  <header class="hdr"><div class="hdr-title">PRESENTATION TITLE GOES HERE</div><div class="hdr-sub">Subtitle goes here</div><div class="brand"><span class="brand-mark"></span>Ridgeline Holdings</div></header>
  <div class="member" style="left:19px;top:78px"><div class="portrait" role="img" aria-label="Team member portrait"></div><div class="label">Lorem Ipsum</div><p class="tiny" style="color:#666">Lorem ipsum dolor sit amet, consectetur adipiscing elit. Aliquam lacus justo</p></div>
  <div class="member" style="left:105px;top:78px"><div class="portrait" role="img" aria-label="Team member portrait"></div><div class="label">Lorem Ipsum</div><p class="tiny" style="color:#666">Lorem ipsum dolor sit amet, consectetur adipiscing elit. Aliquam lacus justo</p></div>
  <div class="member" style="left:191px;top:78px"><div class="portrait" role="img" aria-label="Team member portrait"></div><div class="label">Lorem Ipsum</div><p class="tiny" style="color:#666">Lorem ipsum dolor sit amet, consectetur adipiscing elit. Aliquam lacus justo</p></div>
  <div class="member" style="left:278px;top:78px"><div class="portrait" role="img" aria-label="Team member portrait"></div><div class="label">Lorem Ipsum</div><p class="tiny" style="color:#666">Lorem ipsum dolor sit amet, consectetur adipiscing elit. Aliquam lacus justo</p></div>
  <div class="ftr">www.ridgelineholdings.com</div><div class="pg">11</div><div class="base-line"></div>
</section>

<!-- 5 features -->
<section class="slide c2 r2">
  <header class="hdr"><div class="hdr-title">PRESENTATION TITLE GOES HERE</div><div class="hdr-sub">Subtitle goes here</div><div class="brand"><span class="brand-mark"></span>Ridgeline Holdings</div></header>
  <p class="lead" style="top:48px">Lorem ipsum dolor sit amet, consectetur adipiscing elit. Aliquam lacus justo, vulputate consequat laoreet eget, hendrerit in metus. Sed consectetur lorem mi, id faucibus urna posuere lacinia. Proin a augue viverra, porttitor nulla at, facilisis lorem.</p>
  <div class="feature" style="left:7px;top:80px"><div class="icon-disc"><svg width="20" height="16" viewBox="0 0 20 16" fill="none" stroke="#fff" stroke-width="1.2"><rect x="1" y="2" width="18" height="12" rx="1"/><line x1="1" y1="6" x2="19" y2="6"/><line x1="4" y1="10" x2="10" y2="10"/></svg></div><div class="label">Lorem Ipsum</div><p class="tiny">Lorem ipsum dolor sit amet, consectetur adipiscing elit. Aliquam lacus justo</p></div>
  <div class="feature" style="left:77px;top:80px"><div class="icon-disc"><svg width="20" height="16" viewBox="0 0 20 16" fill="none" stroke="#fff" stroke-width="1.2"><rect x="1" y="2" width="18" height="12" rx="1"/><polyline points="1,3 10,9 19,3"/></svg></div><div class="label">Lorem Ipsum</div><p class="tiny">Lorem ipsum dolor sit amet, consectetur adipiscing elit. Aliquam lacus justo</p></div>
  <div class="feature" style="left:147px;top:80px"><div class="icon-disc"><svg width="22" height="16" viewBox="0 0 22 16" fill="none" stroke="#fff" stroke-width="1.2"><ellipse cx="8" cy="7" rx="7" ry="5"/><ellipse cx="15" cy="9" rx="6" ry="4.5"/></svg></div><div class="label">Lorem Ipsum</div><p class="tiny">Lorem ipsum dolor sit amet, consectetur adipiscing elit. Aliquam lacus justo</p></div>
  <div class="feature" style="left:218px;top:80px"><div class="icon-disc"><svg width="14" height="20" viewBox="0 0 14 20" fill="none" stroke="#fff" stroke-width="1.2"><path d="M7 1 L11 7 L11 14 L3 14 L3 7 Z"/><line x1="7" y1="15" x2="7" y2="19"/></svg></div><div class="label">Lorem Ipsum</div><p class="tiny">Lorem ipsum dolor sit amet, consectetur adipiscing elit. Aliquam lacus justo</p></div>
  <div class="feature" style="left:288px;top:80px"><div class="icon-disc"><svg width="12" height="20" viewBox="0 0 12 20" fill="none" stroke="#fff" stroke-width="1.2"><rect x="1" y="1" width="10" height="18" rx="1.5"/><line x1="5" y1="16" x2="7" y2="16"/></svg></div><div class="label">Lorem Ipsum</div><p class="tiny">Lorem ipsum dolor sit amet, consectetur adipiscing elit. Aliquam lacus justo</p></div>
  <div class="ftr">www.ridgelineholdings.com</div><div class="pg">11</div><div class="base-line"></div>
</section>

<!-- 6 petals -->
<section class="slide c3 r2">
  <header class="hdr"><div class="hdr-title">PRESENTATION TITLE GOES HERE</div><div class="hdr-sub">Subtitle goes here</div><div class="brand"><span class="brand-mark"></span>Ridgeline Holdings</div></header>
  <div class="petal-note left-note" style="left:48px;top:74px"><b>Title here</b>entrepreneurial activities differ substantially depending on the type of</div>
  <div class="petal-note left-note" style="left:48px;top:134px"><b>Title here</b>entrepreneurial activities differ substantially depending on the type of</div>
  <div class="petal-note right-note" style="left:262px;top:74px"><b>Title here</b>entrepreneurial activities differ substantially depending on the type of</div>
  <div class="petal-note right-note" style="left:262px;top:134px"><b>Title here</b>entrepreneurial activities differ substantially depending on the type of</div>
  <div class="petal p-tl" style="left:126px;top:59px"><svg width="22" height="22" viewBox="0 0 22 22" fill="none" stroke="#fff" stroke-width="2"><circle cx="7" cy="7" r="5"/><line x1="10.5" y1="10.5" x2="20" y2="20"/><line x1="16" y1="16" x2="13" y2="19"/></svg></div>
  <div class="petal p-tr" style="left:186px;top:59px"><svg width="22" height="22" viewBox="0 0 22 22" fill="none" stroke="#fff" stroke-width="2"><line x1="3" y1="3" x2="19" y2="19"/><line x1="19" y1="3" x2="3" y2="19"/></svg></div>
  <div class="petal p-bl" style="left:126px;top:119px"><svg width="24" height="20" viewBox="0 0 24 20" fill="none" stroke="#fff" stroke-width="1.6"><line x1="2" y1="1" x2="2" y2="19"/><line x1="2" y1="3" x2="22" y2="3"/><rect x="5" y="6" width="16" height="9"/></svg></div>
  <div class="petal p-br" style="left:186px;top:119px"><svg width="24" height="16" viewBox="0 0 24 16" fill="#fff"><rect x="4" y="2" width="16" height="6" rx="1"/><rect x="1" y="6" width="22" height="6" rx="1.5"/><rect x="3" y="12" width="2" height="3"/><rect x="19" y="12" width="2" height="3"/></svg></div>
  <div class="ftr">www.ridgelineholdings.com</div><div class="pg">11</div><div class="base-line"></div>
</section>

<!-- 7 unit chart -->
<section class="slide c1 r3">
  <header class="hdr"><div class="hdr-title">PRESENTATION TITLE GOES HERE</div><div class="hdr-sub">Subtitle goes here</div><div class="brand"><span class="brand-mark"></span>Ridgeline Holdings</div></header>
  <p class="lead">Lorem ipsum dolor sit amet, consectetur adipiscing elit. Aliquam lacus justo, vulputate consequat laoreet eget, hendrerit in metus. Sed consectetur lorem mi, id faucibus urna posuere lacinia. Proin a augue viverra, porttitor nulla at, facilisis lorem.</p>
  <div class="units" style="left:38px;top:92px"><i class="unit"></i><i class="unit"></i><i class="unit"></i><i class="unit"></i><i class="unit"></i><i class="unit"></i><i class="unit"></i><i class="unit"></i><i class="unit off"></i><i class="unit off"></i></div>
  <div class="unit-val" style="left:252px;top:99px">= 80%</div>
  <div class="units" style="left:38px;top:150px"><i class="unit"></i><i class="unit"></i><i class="unit"></i><i class="unit"></i><i class="unit"></i><i class="unit"></i><i class="unit off"></i><i class="unit off"></i><i class="unit off"></i><i class="unit off"></i></div>
  <div class="unit-val" style="left:252px;top:157px">= 60%</div>
  <div class="ftr">www.ridgelineholdings.com</div><div class="pg">11</div><div class="base-line"></div>
</section>

<!-- 8 table -->
<section class="slide c2 r3">
  <header class="hdr"><div class="hdr-title">PRESENTATION TITLE GOES HERE</div><div class="hdr-sub">Subtitle goes here</div><div class="brand"><span class="brand-mark"></span>Ridgeline Holdings</div></header>
  <table class="data">
    <thead><tr><th>Item</th><th>Jan</th><th>Feb</th><th>Mar</th><th>Apr</th><th>May</th><th>June</th><th>July</th></tr></thead>
    <tbody>
      <tr><td>Lorem</td><td>xxx</td><td>xxx</td><td>xxx</td><td>xxx</td><td>xxx</td><td>xxx</td><td>xxx</td></tr>
      <tr><td>Lorem</td><td>xxx</td><td>xxx</td><td>xxx</td><td>xxx</td><td>xxx</td><td>xxx</td><td>xxx</td></tr>
      <tr><td>Lorem</td><td>xxx</td><td>xxx</td><td>xxx</td><td>xxx</td><td>xxx</td><td>xxx</td><td>xxx</td></tr>
      <tr><td>Lorem</td><td>xxx</td><td>xxx</td><td>xxx</td><td>xxx</td><td>xxx</td><td>xxx</td><td>xxx</td></tr>
      <tr><td>Lorem</td><td>xxx</td><td>xxx</td><td>xxx</td><td>xxx</td><td>xxx</td><td>xxx</td><td>xxx</td></tr>
      <tr><td>Lorem</td><td>xxx</td><td>xxx</td><td>xxx</td><td>xxx</td><td>xxx</td><td>xxx</td><td>xxx</td></tr>
      <tr class="total"><td>Total</td><td>xxx</td><td>xxx</td><td>xxx</td><td>xxx</td><td>xxx</td><td>xxx</td><td>xxx</td></tr>
    </tbody>
  </table>
  <div class="ftr">www.ridgelineholdings.com</div><div class="pg">11</div><div class="base-line"></div>
</section>

<!-- 9 donuts -->
<section class="slide c3 r3">
  <header class="hdr"><div class="hdr-title">PRESENTATION TITLE GOES HERE</div><div class="hdr-sub">Subtitle goes here</div><div class="brand"><span class="brand-mark"></span>Ridgeline Holdings</div></header>
  <div class="stat" style="left:33px"><svg width="56" height="56" viewBox="0 0 56 56"><circle cx="28" cy="28" r="24" fill="none" stroke="var(--track)" stroke-width="5"/><circle cx="28" cy="28" r="24" fill="none" stroke="var(--navy)" stroke-width="5" stroke-dasharray="120.6 150.8" transform="rotate(-90 28 28)"/><text x="28" y="32" text-anchor="middle" font-size="12" font-weight="700" fill="var(--navy)" font-family="Open Sans, sans-serif">80%</text></svg><div class="amount">$908</div><p class="tiny">Ria qui del ium aut ex et estrum nonsequis volupta doluptas illuptas magnam autem volupidit eatem aliqui quas asse eritatae. Nequuntis</p></div>
  <div class="stat" style="left:110px"><svg width="56" height="56" viewBox="0 0 56 56"><circle cx="28" cy="28" r="24" fill="none" stroke="var(--track)" stroke-width="5"/><circle cx="28" cy="28" r="24" fill="none" stroke="var(--blue-mid)" stroke-width="5" stroke-dasharray="73.9 150.8" transform="rotate(-90 28 28)"/><text x="28" y="32" text-anchor="middle" font-size="12" font-weight="700" fill="var(--blue-mid)" font-family="Open Sans, sans-serif">49%</text></svg><div class="amount">$522</div><p class="tiny">Ria qui del ium aut ex et estrum nonsequis volupta doluptas illuptas magnam autem volupidit eatem aliqui quas asse eritatae. Nequuntis</p></div>
  <div class="stat" style="left:187px"><svg width="56" height="56" viewBox="0 0 56 56"><circle cx="28" cy="28" r="24" fill="none" stroke="var(--track)" stroke-width="5"/><circle cx="28" cy="28" r="24" fill="none" stroke="var(--ink)" stroke-width="5" stroke-dasharray="135.7 150.8" transform="rotate(-90 28 28)"/><text x="28" y="32" text-anchor="middle" font-size="12" font-weight="700" fill="var(--ink)" font-family="Open Sans, sans-serif">90%</text></svg><div class="amount">$984</div><p class="tiny">Ria qui del ium aut ex et estrum nonsequis volupta doluptas illuptas magnam autem volupidit eatem aliqui quas asse eritatae. Nequuntis</p></div>
  <div class="stat" style="left:264px"><svg width="56" height="56" viewBox="0 0 56 56"><circle cx="28" cy="28" r="24" fill="none" stroke="var(--track)" stroke-width="5"/><circle cx="28" cy="28" r="24" fill="none" stroke="var(--grey)" stroke-width="5" stroke-dasharray="45.2 150.8" transform="rotate(-90 28 28)"/><text x="28" y="32" text-anchor="middle" font-size="12" font-weight="700" fill="#555" font-family="Open Sans, sans-serif">30%</text></svg><div class="amount">$357</div><p class="tiny">Ria qui del ium aut ex et estrum nonsequis volupta doluptas illuptas magnam autem volupidit eatem aliqui quas asse eritatae. Nequuntis</p></div>
  <div class="ftr">www.ridgelineholdings.com</div><div class="pg">11</div><div class="base-line"></div>
</section>

<!-- 10 quote / section -->
<section class="slide c1 r4 dark">
  <div class="photo" role="img" aria-label="Upward view of city office towers tinted navy" style="inset:0;background:linear-gradient(180deg,#3a3f8e 0%,#2f3382 45%,#4a4f9a 75%,#2a2e78 100%)"></div>
  <svg class="abs" style="left:36px;top:78px" width="66" height="58" viewBox="0 0 66 58"><ellipse cx="40" cy="22" rx="22" ry="18" fill="none" stroke="#fff" stroke-width="3"/><ellipse cx="26" cy="30" rx="24" ry="20" fill="#fff"/><path d="M10 44 L6 56 L20 48 Z" fill="#fff"/></svg>
  <div class="dark-text big-title" style="left:115px;top:86px;font-size:12px;color:#fff">Presentation Title Goes Here</div>
  <p class="dark-text" style="left:115px;top:102px;width:225px;font-size:5.6px;line-height:1.4">Lorem ipsum dolor sit amet, consectetur adipiscing elit. Aliquam lacus justo, vulputate consequat laoreet eget, hendrerit in metus. Sed consectetur lorem mi, id faucibus urna posuere lacinia.</p>
</section>

<!-- 11 section divider -->
<section class="slide c2 r4 dark">
  <div class="abs" style="left:25px;top:0;width:1px;height:131px;background:rgba(255,255,255,.7)"></div>
  <div class="abs" style="left:23px;top:130px;width:5px;height:5px;border-radius:50%;background:#fff"></div>
  <div class="dark-text" style="left:23px;top:141px;font-family:'Roboto',sans-serif;font-weight:300;font-size:12px">PRESENTATION TITLE GOES HERE</div>
  <p class="dark-text" style="left:23px;top:155px;width:220px;font-size:5.6px;line-height:1.4">Lorem ipsum dolor sit amet, consectetur adipiscing elit. Aliquam lacus justo, vulputate consequat laoreet eget, hendrerit in metus. Sed consectetur lorem mi, id faucibus urna posuere lacinia.</p>
</section>

<!-- 12 thank you -->
<section class="slide c3 r4">
  <div class="photo" role="img" aria-label="Softly blurred living room interior with navy tint" style="inset:0;background:linear-gradient(180deg,#4a4677 0%,#5a4f72 45%,#6b5566 75%,#3d3556 100%)"></div>
  <div class="photo" style="inset:0;background:rgba(47,51,130,.45)"></div>
  <div class="brand" style="left:0;right:0;top:82px;justify-content:center;font-size:7px;color:#fff"><span class="brand-mark" style="width:7px;height:7px"></span>Ridgeline Holdings</div>
  <div class="dark-text big-title" style="left:0;right:0;top:104px;text-align:center;font-size:17px;color:#fff">Thank You</div>
  <p class="dark-text" style="left:70px;right:70px;top:128px;text-align:center;font-size:5.6px;line-height:1.4">Lorem ipsum dolor sit amet, consectetur adipiscing elit. Aliquam lacus justo, vulputate consequat laoreet eget, hendrerit in metus. Sed consectetur lorem mi, id faucibus urna posuere lacinia.</p>
</section>

</div>
</body>
</html>
```